Health & Beauty Company- Business Card Design

Two-sided business card design and logo design.

Company markets and sells otc treatments for the health and beauty industry. Marketing products to doctors, pharmacists and retail drug companies like dorvellas, pmn and velo mart.

Designs should be submitted as vector based PDFs. To keep your text in vector format, our printer recommends applications like Adobe Illustrator, Adobe InDesign and more recent versions of Adobe Photoshop.

Target Market(s)

Drug stores, doctors and pharmacists

Industry/Entity Type

Printer

Requirements
Must have
• Back side of business card should include company logo and our tagline: "Reimagining the Care & Wellness Routine"

Company name acronym must be included: NRTK

```html
<!DOCTYPE html>
<html lang="en">
<head>
<meta charset="utf-8">
<title>NRTK Business Card</title>
<link href="https://fonts.googleapis.com/css2?family=Open+Sans:wght@400;600;700&display=swap" rel="stylesheet">
<style>
  :root {
    --bg: #ece7de;
    --card-brown: #725719;
    --card-white: #ffffff;
    --accent-gold: #f2b705;
    --text-light: #ffffff;
    --text-brown: #6f5417;
  }
  * { margin: 0; padding: 0; box-sizing: border-box; }
  html, body {
    width: 1200px; height: 1000px; overflow: hidden;
    background: var(--bg);
    font-family: "Open Sans", Arial, sans-serif;
  }
  .canvas { position: relative; width: 1200px; height: 1000px; }
  .card {
    position: absolute; width: 748px; height: 441px;
    border-radius: 14px; overflow: hidden;
    background: var(--card-brown);
    box-shadow: 0 6px 18px rgba(0,0,0,.25);
  }
  .card-front { left: 48px; top: 27px; }
  .card-back { left: 385px; top: 503px; }
  .abs { position: absolute; white-space: nowrap; line-height: 1; }

  .front-mark {
    left: 165px; top: 150px; width: 100px; height: 100px;
    border-radius: 50%; background: var(--accent-gold);
  }
  .front-name { left: 338px; top: 160px; font-size: 90px; font-weight: 400; color: var(--text-light); }
  .front-tagline { left: 207px; top: 253px; font-size: 19px; color: var(--text-light); }
  .front-web { left: 289px; top: 390px; font-size: 20px; color: var(--text-light); }

  .back-curve { position: absolute; left: 0; top: 0; }
  .back-info { color: var(--text-light); }
  .person-name { left: 37px; top: 126px; font-size: 29px; font-weight: 400; }
  .info-line { font-size: 16px; }
  .info-line.bold { font-weight: 700; }
  .icon { position: absolute; width: 17px; height: 17px; }

  .back-mark {
    left: 442px; top: 159px; width: 64px; height: 64px;
    border-radius: 50%; background: var(--accent-gold);
  }
  .back-name { left: 553px; top: 180px; font-size: 52px; color: var(--text-brown); }
  .back-tagline { left: 470px; top: 237px; font-size: 13px; color: var(--text-brown); }
</style>
</head>
<body>
<div class="canvas">

  <section class="card card-front">
    <div class="abs front-mark"></div>
    <div class="abs front-name">NRTK</div>
    <div class="abs front-tagline">Reimagining the Care &amp; Wellness Routine</div>
    <div class="abs front-web">www.nrtk.com</div>
  </section>

  <section class="card card-back">
    <svg class="back-curve" width="748" height="441" viewBox="0 0 748 441">
      <path d="M481 0 C410 50 370 150 390 260 C405 340 470 410 548 441 L748 441 L748 0 Z" fill="var(--card-white)"/>
    </svg>

    <div class="back-info">
      <div class="abs person-name">Name xxxxx</div>
      <div class="abs info-line" style="left:37px;top:159px">President &amp; CEO</div>
      <div class="abs info-line" style="left:37px;top:184px">address xxxxxxxxx</div>
      <div class="abs info-line" style="left:37px;top:208px">City,State Zip Code</div>

      <svg class="icon" style="left:37px;top:241px" viewBox="0 0 24 24"><path fill="var(--accent-gold)" d="M6.6 10.8a15 15 0 0 0 6.6 6.6l2.2-2.2a1 1 0 0 1 1-.25 11 11 0 0 0 3.6.6 1 1 0 0 1 1 1V20a1 1 0 0 1-1 1A17 17 0 0 1 3 4a1 1 0 0 1 1-1h3.5a1 1 0 0 1 1 1c0 1.25.2 2.45.6 3.6a1 1 0 0 1-.25 1z"/></svg>
      <div class="abs info-line" style="left:59px;top:242px">555 014 720</div>

      <svg class="icon" style="left:37px;top:267px" viewBox="0 0 24 24"><rect x="6" y="2" width="12" height="20" rx="2" fill="var(--accent-gold)"/><rect x="8" y="5" width="8" height="11" fill="var(--card-brown)"/><circle cx="12" cy="19" r="1.2" fill="var(--card-brown)"/></svg>
      <div class="abs info-line" style="left:59px;top:268px">555-310-4472</div>

      <svg class="icon" style="left:37px;top:291px" viewBox="0 0 24 24"><circle cx="12" cy="12" r="10" fill="var(--accent-gold)"/></svg>
      <div class="abs info-line" style="left:59px;top:292px">555-310-4472</div>

      <div class="abs info-line bold" style="left:37px;top:318px">Reimagining the Care &amp; Wellness Routine</div>

      <svg class="icon" style="left:37px;top:344px" viewBox="0 0 24 24"><rect x="2" y="5" width="20" height="14" rx="1.5" fill="var(--accent-gold)"/><path d="M3 6l9 7 9-7" fill="none" stroke="var(--card-brown)" stroke-width="1.8"/></svg>
      <div class="abs info-line" style="left:59px;top:343px">firstname.lastname@nrtkmail.in</div>

      <svg class="icon" style="left:37px;top:369px" viewBox="0 0 24 24"><circle cx="12" cy="12" r="10" fill="none" stroke="var(--accent-gold)" stroke-width="2"/><ellipse cx="12" cy="12" rx="4.5" ry="10" fill="none" stroke="var(--accent-gold)" stroke-width="1.6"/><path d="M2 12h20M4 7h16M4 17h16" stroke="var(--accent-gold)" stroke-width="1.6"/></svg>
      <div class="abs info-line" style="left:59px;top:368px">www.nrtk.com</div>
    </div>

    <div class="abs back-mark"></div>
    <div class="abs back-name">NRTK</div>
    <div class="abs back-tagline">Reimagining the Care &amp; Wellness Routine</div>
  </section>

</div>
</body>
</html>
```